Brisk Meadow Home Page (A Home Wellness e-commerce site & blog)

We need a dynamic home page created for a home wellness brand. Must be visually appealing and extremely mobile-friendly. Logos and a Navmap have been provided but that is just a guideline, PLEASE USE YOUR CREATIVITY.

Target Market(s)

1st target demo: females 24-48, 2nd target demo: all 24-48

Number of Pages Required

1 page

```html
<!DOCTYPE html>
<html lang="en">
<head>
<meta charset="utf-8">
<title>Brisk Meadow – Home Wellness</title>
<link href="https://fonts.googleapis.com/css2?family=Montserrat:wght@600;700;800&family=Roboto:wght@400;500;700&display=swap" rel="stylesheet">
<style>
:root{
  --purple:#4a1a8e;
  --purple-deep:#3a1275;
  --teal:#2db3bd;
  --teal-soft:#45c0c4;
  --lavender:#e7e3f3;
  --ink:#222;
  --muted:#555;
  --footer:#1b1420;
  --white:#fff;
}
*{box-sizing:border-box;margin:0;padding:0}
html,body{width:1200px;height:4494px;overflow:hidden}
body{position:relative;font-family:"Roboto",sans-serif;color:var(--ink);background:var(--white)}
.abs{position:absolute}
.head-font{font-family:"Montserrat",sans-serif}

/* top bar */
.promo-bar{left:0;top:0;width:1200px;height:38px;display:flex;align-items:center;justify-content:center;font:700 13px "Roboto",sans-serif;letter-spacing:.3px}

/* header */
.site-header{left:0;top:38px;width:1200px;height:110px;background:var(--purple)}
.brand{left:113px;top:30px;display:flex;align-items:center;gap:12px;color:var(--white);font:700 40px "Montserrat",sans-serif}
.brand-dot{width:22px;height:22px;background:var(--teal);border-radius:50%}
.contact-strip{left:541px;top:0;width:659px;height:53px;background:var(--teal);border-bottom-left-radius:6px}
.phone-pill{left:10px;top:8px;width:40px;height:40px;border-radius:50%;background:var(--white);display:flex;align-items:center;justify-content:center}
.phone-num{left:64px;top:14px;color:var(--white);font:600 21px "Montserrat",sans-serif}
.social-row{left:330px;top:13px;display:flex;gap:12px}
.social-row span{width:28px;height:28px;border-radius:50%;background:rgba(255,255,255,.3)}
.main-nav{left:539px;top:72px;display:flex;gap:25px;color:var(--white);font:700 13px "Montserrat",sans-serif}
.main-nav .active{color:var(--teal);position:relative}
.main-nav .active::after{content:"";position:absolute;left:4px;top:22px;width:34px;height:8px;border-bottom:3px solid var(--teal);border-radius:0 0 20px 20px}

/* hero */
.hero-photo{left:0;top:148px;width:1200px;height:660px;background:linear-gradient(135deg,#2f4a22 0%,#5a7a37 40%,#8fab5d 70%,#4b6a2e 100%)}
.hero-badge{left:103px;top:222px;width:446px;height:446px;border-radius:50%;background:rgba(45,179,189,.9)}
.hero-title{left:103px;top:362px;width:446px;text-align:center;color:var(--white);font:800 40px/51px "Montserrat",sans-serif}
.btn{display:flex;align-items:center;justify-content:center;border-radius:30px;font:700 16px "Montserrat",sans-serif;color:var(--white)}
.btn-purple{background:var(--purple)}
.btn-teal{background:var(--teal)}
.hero-btn{left:230px;top:543px;width:193px;height:57px}
.slider-arrow{top:478px}
.sale-band{left:0;top:700px;width:1200px;height:477px;background:linear-gradient(180deg,#38b4bb,#4ac1c2)}
.sale-photo{left:0;top:780px;width:1200px;height:397px;background:linear-gradient(90deg,rgba(60,160,120,.35),rgba(74,193,194,0) 30%,rgba(74,193,194,0) 70%,rgba(60,150,110,.35))}
.sale-text{left:600px;top:893px;color:var(--white);font:700 25px/37px "Montserrat",sans-serif}
.sale-btn{left:602px;top:1025px;width:193px;height:54px}

/* section heads */
.eyebrow{color:var(--teal);font:500 14px "Roboto",sans-serif;text-transform:uppercase;text-align:center;left:0;width:1200px}
.section-title{color:var(--purple);font:800 34px/42px "Montserrat",sans-serif;text-align:center;left:0;width:1200px;text-transform:uppercase}
.smile{width:40px;height:10px;border-bottom:4px solid var(--teal);border-radius:0 0 30px 30px}

/* grid */
.tile{position:absolute}
.tile-caption{position:absolute;left:12px;bottom:14px;color:var(--white);font:700 16px/28px "Montserrat",sans-serif;text-transform:uppercase}

/* about */
.about-band{left:0;top:2157px;width:849px;height:572px;background:linear-gradient(90deg,var(--purple-deep),#5a2aa0)}
.about-photo{left:628px;top:2232px;width:572px;height:422px;background:linear-gradient(90deg,#6e8c78,#c9935c 50%,#e3b383)}
.about-label{left:94px;top:2250px;color:var(--teal);font:500 14px "Roboto",sans-serif}
.about-title{left:94px;top:2286px;color:var(--white);font:800 25px/39px "Montserrat",sans-serif}
.about-body{left:94px;top:2396px;width:500px;color:var(--white);font:400 15px/30px "Roboto",sans-serif}
.about-btn{left:94px;top:2576px;width:194px;height:54px}

/* payment */
.pay-body{left:160px;top:2935px;width:880px;text-align:center;color:#333;font:400 15px/30px "Roboto",sans-serif}
.pay-badge{left:495px;top:3075px;width:210px;height:76px;background:var(--white);box-shadow:0 4px 18px rgba(0,0,0,.12);display:flex;align-items:center;justify-content:center;gap:12px;font:700 34px "Montserrat",sans-serif;color:#111}
.pay-badge span{width:40px;height:40px;border-radius:50%;background:#4b3cf0}

/* blogs */
.blog-band{left:0;top:3247px;width:1200px;height:820px;background:var(--lavender)}
.blog-card{position:absolute;top:3465px;width:313px;height:426px;background:var(--white);border-radius:6px;box-shadow:0 3px 12px rgba(0,0,0,.08)}
.blog-img{position:absolute;left:6px;top:6px;width:301px;height:197px;border-radius:4px}
.blog-title{position:absolute;left:8px;top:222px;width:300px;font:700 16px/30px "Montserrat",sans-serif;text-transform:uppercase;color:#1a1a1a}
.blog-text{position:absolute;left:8px;top:290px;width:295px;font:400 13px/30px "Roboto",sans-serif;color:#333}
.blog-link{position:absolute;left:10px;top:384px;font:700 13px "Roboto",sans-serif;color:var(--purple);text-decoration:underline}
.blog-arrow{position:absolute;top:3531px;width:40px;height:40px;border-radius:50%;display:flex;align-items:center;justify-content:center}

/* footer */
.site-footer{left:0;top:3990px;width:1200px;height:504px}
.foot-brand{left:70px;top:4190px;color:var(--white);font:700 38px "Montserrat",sans-serif}
.foot-social{left:86px;top:4255px;display:flex;gap:27px}
.foot-social span{width:29px;height:29px;border-radius:50%;background:var(--teal)}
.foot-head{color:var(--teal);font:700 16px "Montserrat",sans-serif;letter-spacing:.3px}
.foot-list{list-style:none;color:var(--white);font:400 15px/30px "Roboto",sans-serif}
.foot-list li::before{content:"»";color:var(--teal);margin-right:14px}
.foot-contact{color:var(--white);font:400 15px/30px "Roboto",sans-serif}
.foot-icon{width:32px;height:32px;border-radius:50%;background:var(--teal);position:absolute}
.news-field{left:849px;top:4236px;width:272px;height:42px;background:var(--white);border-radius:3px;font:400 12px "Roboto",sans-serif;color:#777;padding:15px 14px}
.news-send{left:1065px;top:4236px;width:56px;height:42px;background:var(--teal);border-radius:0 3px 3px 0}
.chat-bubble{left:1047px;top:4315px;width:53px;height:53px;border-radius:50%;background:var(--teal)}
.foot-rule{left:80px;top:4396px;width:1034px;height:1px;background:rgba(255,255,255,.35)}
.foot-legal{top:4412px;color:var(--white);font:400 13px "Roboto",sans-serif}
</style>
</head>
<body>

<div class="abs promo-bar">FREE SHIPPING ON ALL ORDERS $50 AND OVER!</div>

<header class="abs site-header">
  <div class="abs brand"><span class="brand-dot"></span>Brisk Meadow</div>
  <div class="abs contact-strip">
    <div class="abs phone-pill">
      <svg width="18" height="18" viewBox="0 0 24 24"><path fill="#4a1a8e" d="M6.6 10.8a15 15 0 0 0 6.6 6.6l2.2-2.2c.3-.3.7-.4 1-.2 1.1.4 2.3.6 3.6.6.6 0 1 .4 1 1V20c0 .6-.4 1-1 1A17 17 0 0 1 3 4c0-.6.4-1 1-1h3.5c.6 0 1 .4 1 1 0 1.3.2 2.5.6 3.6.1.3 0 .7-.2 1z"/></svg>
    </div>
    <div class="abs phone-num">+ 123 456 7890</div>
    <div class="abs social-row"><span></span><span></span><span></span><span></span><span></span></div>
  </div>
  <nav class="abs main-nav">
    <span class="active">HOME</span><span>ABOUT US</span><span>PAGES</span><span>PORTFOLIO</span><span>BLOG</span><span>SHOP</span><span>CONTACT US</span>
  </nav>
</header>

<section>
  <div class="abs sale-band"></div>
  <div class="abs hero-photo" role="img" aria-label="Smiling couple jogging together on a forest trail"></div>
  <svg class="abs" style="left:0;top:690px" width="1200" height="130" viewBox="0 0 1200 130">
    <path d="M0 20 Q 600 180 1200 0 L1200 130 L0 130Z" fill="#38b4bb"/>
    <path d="M0 20 Q 600 180 1200 0" fill="none" stroke="#4a1a8e" stroke-width="10"/>
  </svg>
  <div class="abs hero-badge"></div>
  <h1 class="abs hero-title">THEY SAY THAT<br>HOME IS WHERE<br>THE HEART</h1>
  <div class="abs btn btn-purple hero-btn">SHOP NOW</div>
  <svg class="abs slider-arrow" style="left:36px" width="22" height="40" viewBox="0 0 22 40"><path d="M20 2 2 20l18 18" fill="none" stroke="#fff" stroke-width="2"/></svg>
  <svg class="abs slider-arrow" style="left:1142px" width="22" height="40" viewBox="0 0 22 40"><path d="M2 2l18 18L2 38" fill="none" stroke="#fff" stroke-width="2"/></svg>

  <div class="abs sale-photo" role="img" aria-label="Wooden board with green leaves and skincare jars"></div>
  <p class="abs sale-text">50% OFF SALE GOING ON NOW!<br>BECAUSE SAVING MONEY ALSO<br>MAKES US HAPPY.</p>
  <div class="abs btn btn-purple sale-btn">SHOP NOW</div>
</section>

<section>
  <p class="abs eyebrow" style="top:1270px">Our Featured Product</p>
  <h2 class="abs section-title" style="top:1299px">The key to total bliss is nurturing<br>the mind, body, and soul</h2>
  <div class="abs smile" style="left:580px;top:1382px"></div>

  <div class="tile" style="left:115px;top:1435px;width:318px;height:203px;background:linear-gradient(135deg,#eef0ee,#cfd3cf)" role="img" aria-label="White soap bars and folded towel on marble"></div>
  <div class="tile" style="left:441px;top:1435px;width:318px;height:203px;background:linear-gradient(135deg,#5b6a3a,#a87a4c)" role="img" aria-label="Bath tray with candles and plants"></div>
  <div class="tile" style="left:767px;top:1435px;width:318px;height:203px;background:linear-gradient(135deg,#3a3a38,#7a6f62)" role="img" aria-label="Woman applying a charcoal face mask">
    <p class="tile-caption">Lorem ipsum dolor sit amet,<br>consectetur adipisc.</p>
  </div>
  <div class="tile" style="left:115px;top:1648px;width:644px;height:201px;background:linear-gradient(90deg,#f2f2ef,#e8e2d4,#f2f0ea)" role="img" aria-label="Natural ingredients in bowls with lemons and oils"></div>
  <div class="tile" style="left:767px;top:1648px;width:318px;height:413px;background:linear-gradient(160deg,#d9c3b3,#a88a78 60%,#6d5a50)" role="img" aria-label="Woman washing her face at a sink">
    <p class="tile-caption" style="left:22px;bottom:30px">Lorem ipsum dolor sit am<br>et, consectetur adipisc.</p>
  </div>
  <div class="tile" style="left:115px;top:1859px;width:318px;height:202px;background:linear-gradient(135deg,#d6d0c6,#8a6a4e)" role="img" aria-label="Bath products on a wooden table"></div>
  <div class="tile" style="left:441px;top:1859px;width:318px;height:202px;background:linear-gradient(135deg,#e9bfb4,#d6a59a)" role="img" aria-label="Serum bottle and cream jar on pink background"></div>
</section>

<section>
  <div class="abs about-band"></div>
  <div class="abs about-photo" role="img" aria-label="Woman with a clay face mask beside a cosy interior"></div>
  <p class="abs about-label">ABOUT YOUR BRISK MEADOW</p>
  <h2 class="abs about-title">THEY SAY THAT HOME IS WHERE<br>THE HEART IS.</h2>
  <div class="abs smile" style="left:94px;top:2362px"></div>
  <p class="abs about-body">But home is also where your mind and body reside. At Brisk Meadow we believe that home should be your place of Zen. A respite from the crazy world outside those walls. It is where you recharge your soul so you can approach each day with the focus and energy necessary to conquer the world.</p>
  <div class="abs btn btn-teal about-btn">TELL ME MORE</div>
</section>

<section>
  <p class="abs eyebrow" style="top:2823px">Our Payment</p>
  <h2 class="abs section-title" style="top:2852px">Don’t sweat it. You can pay later.</h2>
  <div class="abs smile" style="left:580px;top:2900px"></div>
  <p class="abs pay-body">Lorem ipsum dolor sit amet, consectetur adipiscing elit, sed do eiusmod tempor incididunt ut labore et dolore magna aliqua. Ut enim ad minim veniam, quis nostrud exercitation ullamco laboris nisi ut aliquip ex ea commodo consequat. Duis aute irure dolor in reprehenderit in voluptate velit esse cillum dolore eu fugiat nulla pariatur. Excepteur sint occaecat cupidatat non proident, sunt in culpa qui officia de</p>
  <div class="abs pay-badge"><span></span>Crumbpay</div>
</section>

<section>
  <div class="abs blog-band"></div>
  <p class="abs eyebrow" style="top:3339px">Our News &amp; Blogs</p>
  <h2 class="abs section-title" style="top:3368px">Our latest blogs</h2>
  <div class="abs smile" style="left:580px;top:3420px"></div>

  <article class="blog-card" style="left:112px">
    <div class="blog-img" style="background:linear-gradient(135deg,#d9d3cf,#a9a19c)" role="img" aria-label="Woman looking into a hand mirror"></div>
    <h3 class="blog-title">Lorem ipsum dolor sit amet<br>nsectetur adipiscing.</h3>
    <p class="blog-text">Lorem ipsum dolor sit amet, consectetur adipiscing elit, sed do eiusmod tempor incididunt ut labore et.</p>
    <span class="blog-link">Learn More</span>
  </article>
  <article class="blog-card" style="left:443px">
    <div class="blog-img" style="background:linear-gradient(135deg,#e6c9c4,#b98f89)" role="img" aria-label="Hands applying hand cream"></div>
    <h3 class="blog-title">Lorem ipsum dolor sit amet<br>nsectetur adipiscing.</h3>
    <p class="blog-text">Lorem ipsum dolor sit amet, consectetur adipiscing elit, sed do eiusmod tempor incididunt ut labore et.</p>
    <span class="blog-link">Learn More</span>
  </article>
  <article class="blog-card" style="left:774px">
    <div class="blog-img" style="background:linear-gradient(135deg,#8fc7b5,#4d9d86)" role="img" aria-label="Skincare flat lay with leaves and brushes"></div>
    <h3 class="blog-title">Lorem ipsum dolor sit amet<br>nsectetur adipiscing.</h3>
    <p class="blog-text">Lorem ipsum dolor sit amet, consectetur adipiscing elit, sed do eiusmod tempor incididunt ut labore et.</p>
    <span class="blog-link">Learn More</span>
  </article>

  <div class="blog-arrow" style="left:90px;background:#fff;box-shadow:0 2px 8px rgba(0,0,0,.15)">
    <svg width="12" height="14" viewBox="0 0 12 14"><path d="M9 1 3 7l6 6" fill="none" stroke="#4a1a8e" stroke-width="2.5"/></svg>
  </div>
  <div class="blog-arrow" style="left:1068px;background:var(--purple)">
    <svg width="12" height="14" viewBox="0 0 12 14"><path d="M3 1l6 6-6 6" fill="none" stroke="#fff" stroke-width="2.5"/></svg>
  </div>
</section>

<footer class="abs site-footer">
  <svg class="abs" style="left:0;top:0" width="1200" height="504" viewBox="0 0 1200 504">
    <path d="M0 100 Q 600 -40 1200 100 L1200 504 L0 504Z" fill="#1b1420"/>
    <path d="M0 100 Q 600 -40 1200 100" fill="none" stroke="#4a1a8e" stroke-width="10"/>
  </svg>
</footer>
<div class="abs foot-brand">Brisk Meadow</div>
<div class="abs foot-social"><span></span><span></span><span></span><span></span></div>

<p class="abs foot-head" style="left:352px;top:4140px">QUICK LINKS</p>
<ul class="abs foot-list" style="left:358px;top:4168px">
  <li>Home</li><li>About Us</li><li>Pages</li><li>Portfolio</li><li>Blog</li><li>Contact Us</li>
</ul>

<p class="abs foot-head" style="left:558px;top:4140px">QUICK LINKS</p>
<span class="foot-icon" style="left:562px;top:4176px"></span>
<svg class="abs" style="left:570px;top:4183px" width="16" height="18" viewBox="0 0 16 18"><path d="M8 1a6 6 0 0 0-6 6c0 4.5 6 10 6 10s6-5.5 6-10a6 6 0 0 0-6-6zm0 8.5A2.5 2.5 0 1 1 8 4.5a2.5 2.5 0 0 1 0 5z" fill="#fff"/></svg>
<p class="abs foot-contact" style="left:608px;top:4168px">123 Lorem ipsum dolor sit<br>et, consectetur adip.</p>
<span class="foot-icon" style="left:562px;top:4248px"></span>
<svg class="abs" style="left:570px;top:4256px" width="16" height="16" viewBox="0 0 24 24"><path fill="#fff" d="M6.6 10.8a15 15 0 0 0 6.6 6.6l2.2-2.2c.3-.3.7-.4 1-.2 1.1.4 2.3.6 3.6.6.6 0 1 .4 1 1V20c0 .6-.4 1-1 1A17 17 0 0 1 3 4c0-.6.4-1 1-1h3.5c.6 0 1 .4 1 1 0 1.3.2 2.5.6 3.6.1.3 0 .7-.2 1z"/></svg>
<p class="abs foot-contact" style="left:608px;top:4249px">123 456 7890</p>
<span class="foot-icon" style="left:562px;top:4307px"></span>
<svg class="abs" style="left:570px;top:4317px" width="16" height="12" viewBox="0 0 16 12"><rect x="0.5" y="0.5" width="15" height="11" rx="1" fill="#fff"/><path d="M1 1l7 5 7-5" fill="none" stroke="#2db3bd" stroke-width="1.5"/></svg>
<p class="abs foot-contact" style="left:608px;top:4308px">hello@briskmeadow.com</p>

<p class="abs foot-head" style="left:849px;top:4140px">SIGN UP FOR OUR NEWSLETTER</p>
<p class="abs foot-contact" style="left:849px;top:4168px;width:290px">Lorem ipsum dolor sit amet, consectet ur adipiscing elit, sed do.</p>
<div class="abs news-field">Enter The Email</div>
<div class="abs news-send"></div>
<svg class="abs" style="left:1083px;top:4248px" width="20" height="18" viewBox="0 0 20 18"><path d="M1 8 19 1l-4 16-5-5-3 4V10l9-7-11 6z" fill="#fff"/></svg>
<div class="abs chat-bubble"></div>
<svg class="abs" style="left:1061px;top:4330px" width="26" height="22" viewBox="0 0 26 22"><ellipse cx="13" cy="10" rx="11" ry="8.5" fill="#fff"/><path d="M6 16l-2 5 6-3z" fill="#fff"/><circle cx="8.5" cy="10" r="1.4" fill="#2db3bd"/><circle cx="13" cy="10" r="1.4" fill="#2db3bd"/><circle cx="17.5" cy="10" r="1.4" fill="#2db3bd"/></svg>

<div class="abs foot-rule"></div>
<p class="abs foot-legal" style="left:88px">© Copyrights 2021 <b style="color:var(--teal)">BRISK MEADOW</b> &nbsp;| &nbsp; All Rights Reserved</p>
<p class="abs foot-legal" style="left:901px">Privacy policy &nbsp;| &nbsp; Terms of Service</p>

</body>
</html>
```